Beauty Page

**UPDATED Brief**
We are looking for a website for a beauty organisation that targets both MEN & WOMAN. The focus of the company is in four main areas:

- Health
* Naturopathy & Remedial Massage
- Body
* Yoga
* Personal Training
* Massage
- Skin
* Skin care products such as Velmoracine
- Beauty
* Waxing
* Eye Treatments

We have attached the logo, (a sample of the website that I did - based on the book) and the sample of the pdf book
Updates

Dear All,

Thank you for your patience regarding the beauty contest. We were not happy with the designs that were submitted to us. We therefore had the Graphic designer to do the pricelist book to get all the colours for the organisation.

We are now happy to relaunch the contest and invite you all to take a look at the brief, download a sample of the book and the website we designed on what I’m looking for (the website is only a draft so I don’t want you to copy it) and let your creative mind go wild and present some suggestions to us.

Thanks

 

Target Market(s)

Woman & Men age 24 - 60

Industry/Entity Type

It Company

Requirements
Must have
• Use of main colours
Black
White
Gray - (CYMK - 65, 58, 57, 37)
Purpleish - Maroon (CYMK - 52, 69, 47, 25)

Use of the three color dots on the page.
(white, maroon & Gray)
Same fonts as the book
- Helvetica LT Std
Should not have
• Logo must not be altered i.e different colours, fonts, shadows etc...

```html
<!DOCTYPE html>
<html lang="en">
<head>
<meta charset="utf-8">
<title>Corvella – Health, Body and Skin Care Centre</title>
<link rel="stylesheet" href="https://fonts.googleapis.com/css2?family=Roboto+Condensed:wght@400;700&family=Quicksand:wght@300;400&family=Mulish:wght@400;600&family=Fredoka:wght@500;600&display=swap">
<style>
:root{
  --maroon:#7a2f5a;
  --maroon-dark:#4f1d3a;
  --maroon-deep:#3a1530;
  --nav:#6e4660;
  --plum:#96306c;
  --pink:#b0478a;
  --gray:#55504f;
  --text:#2a2a2a;
  --paper:#f4f2ef;
  --white:#fff;
}
*{box-sizing:border-box;margin:0;padding:0}
html,body{width:1056px;height:1200px;overflow:hidden}
body{background:var(--paper);font-family:"Mulish",sans-serif;color:var(--text);position:relative}
.abs{position:absolute}

/* Header */
.site-header{left:0;top:0;width:1056px;height:107px;
  background:radial-gradient(ellipse 420px 90px at 480px 40px,rgba(220,120,190,.45),transparent 70%),
  linear-gradient(90deg,var(--maroon-deep),#5a2546 40%,#4a1d3c 70%,#3c1733);}
.brand{left:72px;top:14px;color:var(--white)}
.brand-name{font-family:"Roboto Condensed",sans-serif;font-weight:700;font-size:52px;line-height:50px;letter-spacing:-1px}
.brand-tag{font-family:"Mulish",sans-serif;font-size:15.5px;margin-top:6px}
.phone{right:88px;top:54px;display:flex;align-items:center;gap:8px;color:var(--white);
  font-family:"Quicksand",sans-serif;font-weight:300;font-size:31px;letter-spacing:1px}
.phone svg{width:42px;height:42px}

/* Nav */
.main-nav{left:59px;top:111px;width:939px;height:37px;background:var(--nav);
  display:flex;align-items:center;padding-left:14px;
  font-family:"Roboto Condensed",sans-serif;font-size:16px;color:var(--white)}
.main-nav a{color:inherit;text-decoration:none;margin-right:38px}
.main-nav a.active{background:var(--white);color:var(--nav);border-radius:16px;
  padding:4px 30px;margin-right:18px}
.nav-fold{top:148px;width:0;height:0;border-top:11px solid #a57a95}
.nav-fold.l{left:59px;border-right:13px solid transparent}
.nav-fold.r{left:985px;border-left:13px solid transparent}
.dropdown{left:423px;top:149px;width:165px;height:133px;background:#e8e6e4;border:1px solid #cfcccb;
  padding:5px 6px;font-family:"Roboto Condensed",sans-serif;font-size:14px;z-index:5}
.dropdown li{list-style:none;padding:8px 9px;border-bottom:1px dotted #aaa}
.dropdown li.current{background:var(--maroon-dark);color:var(--white);border:1px solid #b8a0b0}

/* Hero */
.hero{left:86px;top:163px;width:877px;height:443px;background:var(--white);border:1px solid #ddd;padding:7px}
.hero-photo{width:100%;height:100%;background:
  radial-gradient(ellipse 260px 180px at 230px 200px,#c9927a,transparent 70%),
  radial-gradient(ellipse 380px 120px at 520px 230px,#e3b49c,transparent 70%),
  linear-gradient(180deg,#f4f0ee,#f7efe6 70%,#f3dcc2)}
.hero-copy{left:555px;top:370px;color:#4a3540;font-family:"Fredoka",sans-serif;font-weight:500}
.hero-copy .l1{font-size:29px;margin-left:10px;line-height:34px}
.hero-copy .l2{font-size:54px;font-weight:600;color:var(--maroon);line-height:52px;letter-spacing:1px}
.hero-copy .l3{font-size:29px;line-height:36px}
.hero-copy .l3 b{color:var(--maroon);font-weight:600}
.btn{display:inline-block;background:var(--plum);color:var(--white);font-family:"Roboto Condensed",sans-serif;
  font-size:14px;padding:5px 6px;border:1px solid #d7a6c4;text-decoration:none;line-height:16px}
.hero .btn{position:absolute;left:700px;top:356px}

/* Cards */
.card{top:636px;width:281px;height:270px;background:linear-gradient(180deg,#fff,#f8f6f5 75%,var(--paper));overflow:hidden}
.card::before{content:"";position:absolute;left:0;top:0;right:0;height:11px;background:var(--maroon);z-index:1}
.card.events::before{background:var(--pink)}
.card h2{position:absolute;font-family:"Quicksand",sans-serif;font-weight:300;font-size:28px;color:var(--maroon);line-height:29px;z-index:3}
.card.events h2{color:var(--pink)}
.card p{position:absolute;font-size:11.5px;line-height:19px;color:#222;width:170px;z-index:3}
.card p em{color:var(--maroon);font-weight:600}
.card .art{position:absolute;z-index:0}
.card .deco{position:absolute;top:2px;width:52px;height:52px;border-radius:50%;z-index:2}
.card .btn{position:absolute;top:200px;z-index:3}

/* Overview */
.rule{height:1px;background:#ddd}
.overview-icon{left:100px;top:925px;width:52px;height:48px;border-radius:50%;
  background:radial-gradient(circle,#f48a3c,#e2366a 70%,transparent 72%)}
.overview h2{left:156px;top:930px;font-family:"Quicksand",sans-serif;font-weight:300;font-size:31px;color:var(--maroon)}
.overview-line{left:156px;top:966px;width:790px;border-top:1px dotted #bbb}
.overview p{left:93px;width:875px;font-size:11.4px;line-height:17.4px;color:#111}

/* Footer */
.footer-brand{left:96px;top:1150px;color:var(--gray)}
.footer-brand .brand-name{font-size:28px;line-height:27px;letter-spacing:0}
.footer-brand .brand-tag{font-size:8.5px;margin-top:2px}
.footer-links{right:98px;top:1154px;font-family:"Roboto Condensed",sans-serif;font-size:12px;color:#222;text-align:right;line-height:20px}
.footer-links span{margin:0 9px}
</style>
</head>
<body>

<header class="site-header abs">
  <div class="brand abs">
    <div class="brand-name">Corvella</div>
    <div class="brand-tag">Health, Body and Skin Care Centre</div>
  </div>
  <div class="phone abs">
    <svg viewBox="0 0 42 42" aria-hidden="true">
      <circle cx="21" cy="21" r="19" fill="#b3253a" stroke="#fff" stroke-width="2"/>
      <path d="M15 12c-2 2-3 5 0 10s7 8 10 8c2 0 3-1 4-2l-4-4-2 2c-2-1-5-4-6-6l2-2-4-6z" fill="#fff"/>
    </svg>
    <span>08 9400 3172</span>
  </div>
</header>

<nav class="main-nav abs">
  <a class="active" href="#">Home</a>
  <a href="#">About Us</a>
  <a href="#">Health</a>
  <a href="#">Body</a>
  <a href="#">Skin</a>
  <a href="#">Beauty</a>
  <a href="#">Contact Us</a>
</nav>
<div class="nav-fold l abs"></div>
<div class="nav-fold r abs"></div>

<section class="hero abs">
  <div class="hero-photo" role="img" aria-label="Woman relaxing face down during a hot stone massage"></div>
  <a class="btn" href="#">Find more details »</a>
</section>
<div class="hero-copy abs">
  <div class="l1">Encompassing the</div>
  <div class="l2">WHOLE BODY</div>
  <div class="l3">to create a <b>HEALTHIER</b> you</div>
</div>

<ul class="dropdown abs">
  <li class="current">Yoga</li>
  <li>Personal Training</li>
  <li>Massage</li>
</ul>

<article class="card abs" style="left:87px">
  <div class="deco" style="left:218px;background:radial-gradient(circle,transparent 40%,#e0246a 42%,#e0246a 55%,transparent 57%)" role="img" aria-label="Pink rings ornament"></div>
  <h2 style="left:21px;top:23px">Newsletter</h2>
  <p style="left:17px;top:68px">Sign up today and start recieving our monthly news direct to your inbox</p>
  <div class="art" style="left:10px;top:110px;width:265px;height:110px;background:radial-gradient(ellipse at 75% 55%,rgba(243,201,168,.7),rgba(228,228,228,.5) 50%,transparent 75%)" role="img" aria-label="Figure at a laptop receiving newsletters"></div>
  <a class="btn" href="#" style="left:9px">Find more details »</a>
</article>

<article class="card abs" style="left:385px">
  <div class="deco" style="left:212px;background:radial-gradient(circle,#9ad14a,#4e9a2a 60%,transparent 62%)" role="img" aria-label="Green leaves ornament"></div>
  <h2 style="left:22px;top:14px">Products &amp;<br>Services</h2>
  <p style="left:7px;top:84px">Check out our range from<br><em>Corvella</em></p>
  <div class="art" style="left:150px;top:60px;width:131px;height:190px;background:radial-gradient(ellipse at 50% 45%,rgba(217,176,154,.8),rgba(169,214,236,.7) 55%,transparent 75%)" role="img" aria-label="Smiling couple"></div>
  <a class="btn" href="#" style="left:13px">Find more details »</a>
</article>

<article class="card events abs" style="left:683px">
  <div class="deco" style="left:222px;background:radial-gradient(circle,#ffd21c,#f0a800 60%,transparent 62%)" role="img" aria-label="Golden swirl ornament"></div>
  <h2 style="left:14px;top:23px">Special Events</h2>
  <p style="left:8px;top:69px;width:180px"><em>Corvella</em> is available for all your special occassions.</p>
  <div class="art" style="left:0;top:110px;width:281px;height:100px;background:radial-gradient(ellipse at 75% 40%,rgba(230,196,106,.8),rgba(239,230,214,.6) 40%,transparent 70%)" role="img" aria-label="Wedding rings with wedding day lettering"></div>
  <a class="btn" href="#" style="left:13px">Find more details »</a>
</article>

<div class="rule abs" style="left:93px;top:919px;width:868px"></div>
<section class="overview">
  <div class="overview-icon abs" role="img" aria-label="Butterfly ornament"></div>
  <h2 class="abs">Overview</h2>
  <div class="overview-line abs"></div>
  <p class="abs" style="top:985px">Lorem ipsum dolor sit amet, sit lectus blandit non nec egestas nulla, ac ut vitae massa blanditiis pulvinar, aenean enim nec sapien quis velit nunc, nunc fugiat velit purus ligula. In mattis curabitur id at aliquam, pede eu in massa nibh porttitor. Tellus vestibulum nulla nunc nascetur nec, vestibulum ac malesuada velit tempus. Et iaculis ultricies, sapien sapien vitae odio, rutrum arcu. Vitae porttitor dapibus lacus id enim, in nulla, fermentum nec torquent ut erat habitasse.</p>
  <p class="abs" style="top:1055px">Cras felis enim, purus ut turpis, et lacus suspendisse, nullam a curabitur. Pede risus duis, et metus nisl metus pharetra. Et lacinia eget mauris morbi urna esse, pede phasellus leo veniam ut justo. Id arcu cum semper tempus, eget lacus, phasellus conubia duis. Odio nibh hymenaeos laudantium at aptent, voluptate laoreet erat vel dignissim justo.</p>
  <a class="btn abs" href="#" style="left:866px;top:1096px">more details »</a>
</section>

<div class="rule abs" style="left:93px;top:1142px;width:868px"></div>
<footer>
  <div class="footer-brand abs">
    <div class="brand-name">Corvella</div>
    <div class="brand-tag">Health, Body and Skin Care Centre</div>
  </div>
  <div class="footer-links abs">
    <div>Home<span>|</span>About Us<span>|</span>Health<span>|</span>Body<span>|</span>Skin<span>|</span>Beauty<span>|</span>Contact Us</div>
    <div>Corvella © Copyright 2011.&nbsp;&nbsp; Privacy Policy&nbsp; |&nbsp; Terms of Use</div>
  </div>
</footer>

</body>
</html>
```